Eye catching business card using our brand new logo
Dorvik Fabrication, Inc.
Modern
Wendell R. Fostrey
President
58 Quarry Hollow Road
Brindle, NH 03419
WFostrey@norvax.net
We would like to see many different styles of our brand new logo used in our business cards. Some would fill the card with the logo and some using it in the lower left corner of the card

```html
<!DOCTYPE html>
<html lang="en">
<head>
<meta charset="utf-8">
<title>Dorvik Fabrication, Inc. — Business Card</title>
<link href="https://fonts.googleapis.com/css2?family=Roboto+Condensed:wght@700&family=Share+Tech+Mono&family=Roboto:wght@400&display=swap" rel="stylesheet">
<style>
  :root {
    --bg: #2b2b2d;
    --card-silver-1: #f4f5f6;
    --card-silver-2: #d9dbde;
    --steel-dark: #6d7075;
    --steel-mid: #a6a9ae;
    --brand-blue: #2f5fd0;
    --brand-blue-deep: #1c3f9e;
    --ink: #2a2c30;
  }
  * { margin: 0; padding: 0; box-sizing: border-box; }
  html, body { width: 1200px; height: 874px; overflow: hidden; }
  body { background: var(--bg); position: relative; font-family: "Roboto", sans-serif; }

  .card {
    position: absolute;
    width: 560px; height: 320px;
    border-radius: 18px;
    overflow: hidden;
    background: linear-gradient(180deg, var(--card-silver-1), var(--card-silver-2));
    box-shadow: 0 10px 30px rgba(0,0,0,.5);
  }
  .card--front { left: 70px; top: 110px; }
  .card--back  { left: 570px; top: 450px; }

  /* front */
  .front-mark {
    position: absolute; left: -60px; top: 20px;
    width: 300px; height: 300px; border-radius: 50%;
    background: radial-gradient(circle at 35% 35%, #e4e5e7, var(--steel-mid) 55%, var(--steel-dark));
  }
  .front-name {
    position: absolute; left: 290px; top: 40px;
    font-family: "Roboto Condensed", sans-serif; font-weight: 700;
    color: var(--brand-blue); font-size: 30px; line-height: 1.05;
    text-transform: uppercase;
  }

  /* back */
  .back-wave { position: absolute; inset: 0; }
  .back-logo {
    position: absolute; left: 34px; top: 110px;
    display: flex; align-items: center; gap: 12px;
  }
  .back-logo__circle {
    width: 74px; height: 74px; border-radius: 50%;
    background: radial-gradient(circle at 35% 35%, #e4e5e7, var(--steel-mid) 55%, var(--steel-dark));
  }
  .back-logo__name {
    font-family: "Roboto Condensed", sans-serif; font-weight: 700;
    color: var(--brand-blue); font-size: 22px; line-height: 1.05;
    text-transform: uppercase;
  }
  .holder {
    position: absolute; right: 30px; top: 24px; text-align: right; color: var(--ink);
    font-size: 17px;
  }
  .holder__title { font-size: 14px; margin-top: 2px; }
  .contact {
    position: absolute; right: 30px; top: 100px; text-align: right;
    font-family: "Share Tech Mono", monospace; color: var(--ink); font-size: 14px; line-height: 1.55;
  }
  .contact__row { display: flex; justify-content: flex-end; align-items: center; gap: 6px; }
  .address {
    position: absolute; right: 30px; bottom: 26px;
    font-family: "Share Tech Mono", monospace; color: #fff; font-size: 14px; text-align: right; line-height: 1.4;
  }
</style>
</head>
<body>

  <section class="card card--front" aria-label="Card front">
    <div class="front-mark"></div>
    <div class="front-name">Dorvik<br>Fabrication, Inc.</div>
  </section>

  <section class="card card--back" aria-label="Card back">
    <svg class="back-wave" viewBox="0 0 560 320" preserveAspectRatio="none" aria-hidden="true">
      <defs>
        <linearGradient id="waveBlue" x1="0" y1="0" x2="1" y2="1">
          <stop offset="0" stop-color="#3f74e6"/>
          <stop offset="1" stop-color="#1c3f9e"/>
        </linearGradient>
        <linearGradient id="waveSteel" x1="0" y1="0" x2="1" y2="0">
          <stop offset="0" stop-color="#ffffff"/>
          <stop offset=".5" stop-color="#8e9196"/>
          <stop offset="1" stop-color="#d7d9dc"/>
        </linearGradient>
      </defs>
      <path d="M0 250 C160 300 320 210 560 170 L560 320 L0 320 Z" fill="url(#waveSteel)"/>
      <path d="M0 280 C180 320 340 230 560 190 L560 320 L0 320 Z" fill="url(#waveBlue)"/>
    </svg>

    <div class="back-logo">
      <div class="back-logo__circle"></div>
      <div class="back-logo__name">Dorvik<br>Fabrication, Inc.</div>
    </div>

    <div class="holder">
      <div class="holder__name">Wendell R. Fostrey</div>
      <div class="holder__title">President</div>
    </div>

    <div class="contact">
      <div class="contact__row">(603) 555-0142
        <svg width="12" height="12" viewBox="0 0 12 12" aria-hidden="true"><path d="M2 1h3l1 3-2 1a7 7 0 0 0 3 3l1-2 3 1v3c-5 0-9-4-9-9z" fill="#2a2c30"/></svg>
      </div>
      <div class="contact__row">(603) 555-0187
        <svg width="12" height="12" viewBox="0 0 12 12" aria-hidden="true"><rect x="1" y="3" width="10" height="7" fill="#2a2c30"/><rect x="3" y="1" width="6" height="2" fill="#2a2c30"/></svg>
      </div>
      <div class="contact__row">WFostrey@norvax.net
        <svg width="12" height="12" viewBox="0 0 12 12" aria-hidden="true"><rect x="1" y="2" width="10" height="8" fill="#2a2c30"/><path d="M1 2l5 4 5-4" stroke="#fff" fill="none"/></svg>
      </div>
    </div>

    <div class="address">58 Quarry Hollow Road,<br>Brindle, NH 03419</div>
  </section>

</body>
</html>
```